Advertising facade - tanning salon

We need outdoor advertising on the facade of the commercial property of a tanning salon. A stock photo from https://www.brontavel.example/de/social-media-units/k4r/ or https://media.vqt.example/europe-rest-of-world/aktuelle-solarien should / can -and-collarien / k4r-serie / can be used as a background.

The tanning salon logo is already available as an eps or svg file.

The background or the banner itself should be adapted to the facade of the property or give a coherent overall picture.

We need an outdoor advertisement on the facade of the commercial property of a tanning salon.

A stock photo from https://www.brontavel.example/de/social-media-units/k4r/ or https://media.vqt.example/europe-rest-of-world/aktuelle-solarien should / can -and-collarien / k4r-serie / can be used as a background.

The background or the banner should be adapted to the facade of the property or give a coherent overall picture.

Once a graphic is to be made on the commercial property from the outside (see annex outside) and a graphic for a print of a banner measuring 300x60cm.

The logo (see attachment Logo with background or gold frame) should be recognizable as the largest, preferably with a stock photo (see links above in the text) in all or part of the background.
The following should also be written on the logo:
Perfect tan? Now left
Un bronzage parfait? Maintenant à gauche

```html
<!DOCTYPE html>
<html lang="fr">
<head>
<meta charset="utf-8">
<title>Studio Lumiva – Bannière façade</title>
<link href="https://fonts.googleapis.com/css2?family=Montserrat:wght@400;500&display=swap" rel="stylesheet">
<style>
  :root {
    --canvas: #e9e9e7;
    --banner: #1c1c1e;
    --banner-sheen: #2a2a2d;
    --text-light: #f4f4f2;
    --accent-peach: #e9b98c;
    --brand-gold: #c9a24c;
    --photo-dark: #2b2d33;
    --photo-glow: #8fb8d6;
  }
  * { margin: 0; padding: 0; box-sizing: border-box; }
  html, body {
    width: 1200px;
    height: 900px;
    overflow: hidden;
    background: var(--canvas);
    font-family: "Montserrat", sans-serif;
  }
  .facade-banner {
    position: absolute;
    left: 40px;
    top: 333px;
    width: 1120px;
    height: 233px;
    background: linear-gradient(100deg, var(--banner) 0%, var(--banner-sheen) 35%, var(--banner) 60%, var(--banner) 100%);
  }
  .product-photo {
    position: absolute;
    left: 55px;
    top: 17px;
    width: 256px;
    height: 197px;
    border-radius: 10px;
    background: radial-gradient(ellipse at 50% 45%, var(--photo-glow) 0%, #6c7f98 30%, var(--photo-dark) 75%, var(--banner) 100%);
  }
  .headline {
    position: absolute;
    left: 349px;
    top: 72px;
    color: var(--text-light);
    font-weight: 400;
    font-size: 36px;
    line-height: 47px;
    letter-spacing: 0.3px;
  }
  .headline .accent { color: var(--accent-peach); }
  .brand {
    position: absolute;
    left: 793px;
    top: 20px;
    width: 272px;
    height: 180px;
    display: flex;
    align-items: center;
    justify-content: center;
    gap: 12px;
  }
  .brand-dot {
    width: 22px;
    height: 22px;
    border-radius: 50%;
    background: var(--brand-gold);
  }
  .brand-name {
    color: var(--brand-gold);
    font-weight: 500;
    font-size: 28px;
    letter-spacing: 1px;
  }
</style>
</head>
<body>
  <section class="facade-banner">
    <div class="product-photo" role="img" aria-label="Photo de produit : cabine de bronzage ouverte avec tubes lumineux"></div>
    <p class="headline">
      Un bronzage <span class="accent">parfait?</span><br>
      Maintenant <span class="accent">à gauche</span>
    </p>
    <div class="brand">
      <span class="brand-dot"></span>
      <span class="brand-name">Studio Lumiva</span>
    </div>
  </section>
</body>
</html>
```